Professional and creatice Life Coach - Business Card design

I just relaunched my website and now i a need a correspoonding business card for my task as life coach. My website is www.tbalrond.com as reference. The compass is kind of a symbol for my work, as I help people navigate through their challenging phases in life. The business card should be colorful, but not too playful as I also adress business people. So it sould be creative, but professional (also to suport my other business as Management Consultant)

Target Market(s)

People who want to get teir problems resolved, in business, partnership and other personal realms

Industry/Entity Type

Life Coaching

Contact Information for Business Card

Front side should include Name, Phone number, Email, Website and address

Font styles to use
Sans Serif

Colors
add136

Requirements
Must have
• "Mag. Leopold Brantner" -> Name
"Energetische Praxis" -> Jobtitle (describing my profession as life coach)
colours and style should match my website www.tbalrond.com
Nice to have
• a compass as a symbol

```html
<!DOCTYPE html>
<html lang="de">
<head>
<meta charset="utf-8">
<title>Leopold Brantner – Business Card</title>
<link rel="stylesheet" href="https://fonts.googleapis.com/css2?family=Mulish:wght@400;500;600&display=swap">
<style>
  :root {
    --backdrop: #8c8c8c;
    --card: #231f20;
    --green: #4bb749;
    --white: #f2f2f2;
  }
  * { margin: 0; padding: 0; box-sizing: border-box; }
  html, body {
    width: 1200px; height: 960px; overflow: hidden;
    background: var(--backdrop);
    font-family: "Mulish", "Avenir", sans-serif;
  }
  .card {
    position: absolute;
    left: 281px;
    width: 655px;
    height: 373px;
    background: var(--card);
    border-radius: 26px;
  }
  .card--front { top: 59px; }
  .card--back { top: 501px; }

  /* Front: brand block */
  .brand {
    position: absolute;
    left: 90px; top: 125px;
    width: 200px;
    display: flex; flex-direction: column; align-items: center;
  }
  .brand__dot {
    width: 60px; height: 60px; border-radius: 50%;
    background: var(--green);
    margin-bottom: 44px;
  }
  .brand__name {
    color: var(--green);
    font-size: 28px; font-weight: 500;
    white-space: nowrap;
    line-height: 1;
  }
  .divider {
    position: absolute;
    left: 327px; top: 119px;
    width: 2px; height: 134px;
    background: var(--green);
  }
  .details {
    position: absolute;
    left: 354px; top: 117px;
  }
  .details__name {
    color: var(--green);
    font-size: 24px; font-weight: 500;
    line-height: 1.1;
  }
  .details__role {
    color: var(--white);
    font-size: 17px; font-weight: 400;
    margin-top: 3px;
  }
  .contacts {
    list-style: none;
    margin-top: 19px;
  }
  .contacts li {
    display: flex; align-items: center;
    color: var(--white);
    font-size: 16px;
    height: 24px;
  }
  .contacts svg {
    width: 14px; height: 14px;
    margin-right: 7px;
    fill: var(--green);
  }

  /* Back */
  .back-brand {
    position: absolute;
    left: 0; right: 0; top: 96px;
    display: flex; flex-direction: column; align-items: center;
  }
  .back-brand__dot {
    width: 110px; height: 110px; border-radius: 50%;
    background: var(--green);
    margin-bottom: 24px;
  }
  .back-brand__name {
    color: var(--green);
    font-size: 30px; font-weight: 500;
    line-height: 1.2;
  }
  .back-web {
    position: absolute;
    left: 0; right: 0; top: 318px;
    text-align: center;
    color: var(--white);
    font-size: 15px;
    letter-spacing: 1.5px;
  }
</style>
</head>
<body>

<section class="card card--front">
  <div class="brand">
    <span class="brand__dot"></span>
    <span class="brand__name">Leopold Brantner</span>
  </div>

  <span class="divider"></span>

  <div class="details">
    <h1 class="details__name">Mag. Leopold Brantner</h1>
    <p class="details__role">Energetische Praxis</p>
    <ul class="contacts">
      <li>
        <svg viewBox="0 0 16 16"><path d="M4 1l3 3-1.5 2c.8 1.8 2.2 3.2 4 4L11.5 8.5l3 3-2 2.5C6 13 3 10 2 3.5z"/></svg>
        660 482 7719
      </li>
      <li>
        <svg viewBox="0 0 16 16"><path d="M1 4h14v1L8 9 1 5zM1 6.5l7 4 7-4V12H1z"/></svg>
        info@tbalrond.com
      </li>
      <li>
        <svg viewBox="0 0 16 16"><path fill-rule="evenodd" d="M8 1a7 7 0 110 14A7 7 0 018 1zm-1 1.6A5.5 5.5 0 002.6 7H5c.1-1.7.8-3.2 2-4.4zM9 2.6c1.2 1.2 1.9 2.7 2 4.4h2.4A5.5 5.5 0 009 2.6zM8 3c-1 1.1-1.6 2.5-1.7 4h3.4C9.6 5.5 9 4.1 8 3zM2.6 9A5.5 5.5 0 007 13.4C5.8 12.2 5.1 10.7 5 9zm3.7 0c.1 1.5.7 2.9 1.7 4 1-1.1 1.6-2.5 1.7-4zM11 9c-.1 1.7-.8 3.2-2 4.4A5.5 5.5 0 0013.4 9z"/></svg>
        www.tbalrond.com
      </li>
    </ul>
  </div>
</section>

<section class="card card--back">
  <div class="back-brand">
    <span class="back-brand__dot"></span>
    <span class="back-brand__name">Leopold Brantner</span>
  </div>
  <p class="back-web">www.tbalrond.com</p>
</section>

</body>
</html>
```